Ember Card Flyer

Please design a flyer with all the info on attached file. We want the logo in the upper left hand corner and a very simple and clean border. We want it to come across clean and modern. Please submit one with each of the four logos you made for us. Let me know if you have any questions.

```html
<!DOCTYPE html>
<html lang="en">
<head>
<meta charset="utf-8">
<title>Ember Card Flyer</title>
<link rel="stylesheet" href="https://fonts.googleapis.com/css2?family=Arimo:wght@400;700&display=swap">
<style>
  :root {
    --navy: #0d3f8b;
    --navy-edge: #0a2f6a;
    --white: #ffffff;
    --soft-white: rgba(255,255,255,0.55);
    --page: #ffffff;
  }
  * { margin: 0; padding: 0; box-sizing: border-box; }
  html, body {
    width: 1200px;
    height: 424px;
    overflow: hidden;
    background: var(--page);
    font-family: "Arimo", Arial, sans-serif;
    color: var(--white);
  }
  .sheet { position: relative; width: 1200px; height: 424px; }
  .flyer {
    position: absolute;
    top: 2px;
    width: 296px;
    height: 420px;
    background: var(--navy);
    outline: 1px solid var(--navy-edge);
    outline-offset: 2px;
  }
  .flyer:nth-child(1) { left: 3px; }
  .flyer:nth-child(2) { left: 303px; }
  .flyer:nth-child(3) { left: 603px; }
  .flyer:nth-child(4) { left: 903px; }
  .flyer-frame {
    position: absolute;
    inset: 7px;
    border: 1.5px solid var(--white);
  }
  .brand {
    position: absolute;
    top: 22px;
    left: 0;
    right: 0;
    height: 60px;
    display: flex;
    align-items: center;
    justify-content: center;
    gap: 10px;
  }
  .brand-name {
    font-size: 22px;
    font-weight: 700;
    letter-spacing: 0.3px;
  }
  .brand-dot {
    width: 30px;
    height: 30px;
    border-radius: 50%;
    background: var(--white);
  }
  .brand-dot.is-soft {
    width: 40px;
    height: 40px;
    background: var(--soft-white);
  }
  .brand-square {
    width: 30px;
    height: 30px;
    background: var(--white);
  }
  .brand-square.is-small {
    width: 20px;
    height: 20px;
  }
  .divider {
    position: absolute;
    left: 27px;
    width: 242px;
    height: 10px;
  }
  .divider.top { top: 92px; }
  .divider.bottom { top: 372px; }
  .about-title {
    position: absolute;
    top: 106px;
    left: 0; right: 0;
    text-align: center;
    font-size: 16px;
    font-weight: 700;
  }
  .about-text {
    position: absolute;
    top: 131px;
    left: 34px;
    width: 224px;
    font-size: 10.6px;
    line-height: 14.7px;
  }
  .benefits-title {
    position: absolute;
    top: 238px;
    left: 20px;
    font-size: 16px;
    font-weight: 400;
    white-space: nowrap;
  }
  .benefits-list {
    position: absolute;
    top: 259px;
    left: 23px;
    list-style: none;
    font-size: 10.6px;
    line-height: 14.7px;
    white-space: nowrap;
  }
  .web-address {
    position: absolute;
    top: 389px;
    left: 0; right: 0;
    text-align: center;
    font-size: 15px;
    letter-spacing: 0.2px;
  }
</style>
</head>
<body>
<main class="sheet">

  <section class="flyer">
    <div class="flyer-frame"></div>
    <header class="brand">
      <span class="brand-dot"></span>
      <span class="brand-name">Ember Card</span>
    </header>
    <svg class="divider top" viewBox="0 0 242 10"><line x1="6" y1="5" x2="236" y2="5" stroke="#fff" stroke-width="1"/><circle cx="3" cy="5" r="2.5" fill="none" stroke="#fff"/><circle cx="239" cy="5" r="2.5" fill="none" stroke="#fff"/></svg>
    <h2 class="about-title">About us</h2>
    <p class="about-text">The Ember Card is Orange County’s only exclusive Restaurant Loyalty Program. We offer a unique marketing strategy, a strategy that will help you gain new customers, increase traffic into your restaurant and solidify a loyal customer base.</p>
    <h2 class="benefits-title">How The Ember Card benefits you</h2>
    <ul class="benefits-list">
      <li>-No Cost to your Restaurant</li>
      <li>-Fill your tables with quality customers</li>
      <li>-Free marketing and website exposure</li>
      <li>-Gain new customers and solidify customer loyalty</li>
      <li>-Increase traffic during your quiet periods</li>
      <li>-Custom tailor options to fit your restaurants needs</li>
      <li>-Freedom to opt out at any time</li>
    </ul>
    <svg class="divider bottom" viewBox="0 0 242 10"><line x1="6" y1="5" x2="236" y2="5" stroke="#fff" stroke-width="1"/><circle cx="3" cy="5" r="2.5" fill="none" stroke="#fff"/><circle cx="239" cy="5" r="2.5" fill="none" stroke="#fff"/></svg>
    <p class="web-address">WWW.EMBERCARDUSA.COM</p>
  </section>

  <section class="flyer">
    <div class="flyer-frame"></div>
    <header class="brand">
      <span class="brand-square"></span>
      <span class="brand-name">Ember Card</span>
    </header>
    <svg class="divider top" viewBox="0 0 242 10"><line x1="6" y1="5" x2="236" y2="5" stroke="#fff" stroke-width="1"/><circle cx="3" cy="5" r="2.5" fill="none" stroke="#fff"/><circle cx="239" cy="5" r="2.5" fill="none" stroke="#fff"/></svg>
    <h2 class="about-title">About us</h2>
    <p class="about-text">The Ember Card is Orange County’s only exclusive Restaurant Loyalty Program. We offer a unique marketing strategy, a strategy that will help you gain new customers, increase traffic into your restaurant and solidify a loyal customer base.</p>
    <h2 class="benefits-title">How The Ember Card benefits you</h2>
    <ul class="benefits-list">
      <li>-No Cost to your Restaurant</li>
      <li>-Fill your tables with quality customers</li>
      <li>-Free marketing and website exposure</li>
      <li>-Gain new customers and solidify customer loyalty</li>
      <li>-Increase traffic during your quiet periods</li>
      <li>-Custom tailor options to fit your restaurants needs</li>
      <li>-Freedom to opt out at any time</li>
    </ul>
    <svg class="divider bottom" viewBox="0 0 242 10"><line x1="6" y1="5" x2="236" y2="5" stroke="#fff" stroke-width="1"/><circle cx="3" cy="5" r="2.5" fill="none" stroke="#fff"/><circle cx="239" cy="5" r="2.5" fill="none" stroke="#fff"/></svg>
    <p class="web-address">WWW.EMBERCARDUSA.COM</p>
  </section>

  <section class="flyer">
    <div class="flyer-frame"></div>
    <header class="brand">
      <span class="brand-square is-small"></span>
      <span class="brand-name">Ember Card</span>
    </header>
    <svg class="divider top" viewBox="0 0 242 10"><line x1="6" y1="5" x2="236" y2="5" stroke="#fff" stroke-width="1"/><circle cx="3" cy="5" r="2.5" fill="none" stroke="#fff"/><circle cx="239" cy="5" r="2.5" fill="none" stroke="#fff"/></svg>
    <h2 class="about-title">About us</h2>
    <p class="about-text">The Ember Card is Orange County’s only exclusive Restaurant Loyalty Program. We offer a unique marketing strategy, a strategy that will help you gain new customers, increase traffic into your restaurant and solidify a loyal customer base.</p>
    <h2 class="benefits-title">How The Ember Card benefits you</h2>
    <ul class="benefits-list">
      <li>-No Cost to your Restaurant</li>
      <li>-Fill your tables with quality customers</li>
      <li>-Free marketing and website exposure</li>
      <li>-Gain new customers and solidify customer loyalty</li>
      <li>-Increase traffic during your quiet periods</li>
      <li>-Custom tailor options to fit your restaurants needs</li>
      <li>-Freedom to opt out at any time</li>
    </ul>
    <svg class="divider bottom" viewBox="0 0 242 10"><line x1="6" y1="5" x2="236" y2="5" stroke="#fff" stroke-width="1"/><circle cx="3" cy="5" r="2.5" fill="none" stroke="#fff"/><circle cx="239" cy="5" r="2.5" fill="none" stroke="#fff"/></svg>
    <p class="web-address">WWW.EMBERCARDUSA.COM</p>
  </section>

  <section class="flyer">
    <div class="flyer-frame"></div>
    <header class="brand">
      <span class="brand-dot is-soft"></span>
      <span class="brand-name">Ember Card</span>
    </header>
    <svg class="divider top" viewBox="0 0 242 10"><line x1="6" y1="5" x2="236" y2="5" stroke="#fff" stroke-width="1"/><circle cx="3" cy="5" r="2.5" fill="none" stroke="#fff"/><circle cx="239" cy="5" r="2.5" fill="none" stroke="#fff"/></svg>
    <h2 class="about-title">About us</h2>
    <p class="about-text">The Ember Card is Orange County’s only exclusive Restaurant Loyalty Program. We offer a unique marketing strategy, a strategy that will help you gain new customers, increase traffic into your restaurant and solidify a loyal customer base.</p>
    <h2 class="benefits-title">How The Ember Card benefits you</h2>
    <ul class="benefits-list">
      <li>-No Cost to your Restaurant</li>
      <li>-Fill your tables with quality customers</li>
      <li>-Free marketing and website exposure</li>
      <li>-Gain new customers and solidify customer loyalty</li>
      <li>-Increase traffic during your quiet periods</li>
      <li>-Custom tailor options to fit your restaurants needs</li>
      <li>-Freedom to opt out at any time</li>
    </ul>
    <svg class="divider bottom" viewBox="0 0 242 10"><line x1="6" y1="5" x2="236" y2="5" stroke="#fff" stroke-width="1"/><circle cx="3" cy="5" r="2.5" fill="none" stroke="#fff"/><circle cx="239" cy="5" r="2.5" fill="none" stroke="#fff"/></svg>
    <p class="web-address">WWW.EMBERCARDUSA.COM</p>
  </section>

</main>
</body>
</html>
```